Zielgruppe
Wir sind ein Fliesenlegerbetrieb und sind auf der suche nach Mitarbeitern / Fliesenleger. Unsere Kunden sind Privatkunden sowie Öffentliche und Gewerbliche Auftraggeber. Das design soll für Arbeitsuchende ansprechend sein und zu unserem CI passen. Inspiration zu unserem CI finden SIe unter www.fliesen-worlak.de
Aufgabenstellung
Es handelt sich um eine Stellenanzeige die wir im Format 90x50 mm quer und im Format 90 x 90 mm benötigen. In Farbe und S/W.
Unser Textvorschlag, Der Designer darf aucg selbst kreativ sein / werden.
Du arbeitest selbständig und verantwortungsbewusst, hast Freude am Kundenkontakt und kannst jedes Problem lösen ? Dann komm direkt zu uns !
Das erwartet Dich bei uns:
- Junges eingespieltes Team
- Sehr gutes Betriebsklima
- Faire Bezahlung
- Baustellenfahrzeug + Werkzeug
- Unbefristetes Arbeitsverhältnis
- Heimatnahe Baustellen
- Öffentliche, Gewerbliche, Private Baustellen
Kontaktdaden damit sich der Bewerber auch bei uns melden kann !

```html
<!DOCTYPE html>
<html lang="de">
<head>
<meta charset="utf-8">
<title>Stellenanzeige Fliesenleger – Fliesen-Worlak</title>
<link href="https://fonts.googleapis.com/css2?family=Rubik:wght@500;600&family=Nunito:wght@900&family=Figtree:wght@300;400&display=swap" rel="stylesheet">
<style>
  :root{
    --red:#d2313a;
    --red-light:#ee4f57;
    --red-dark:#c32a32;
    --dark:#262628;
    --dark-light:#3a3a3d;
    --ink:#1c1c1c;
    --white:#ffffff;
    --photo-a:#c9c8c4;
    --photo-b:#5b5c5e;
    --photo-c:#2b2c2e;
  }
  *{box-sizing:border-box;margin:0;padding:0}
  html,body{width:1200px;height:1117px;overflow:hidden}
  body{
    background:radial-gradient(ellipse at 60% 55%,#b9b9b9 0%,#a3a3a3 45%,#8a8a8a 100%);
    position:relative;font-family:"Figtree",sans-serif;color:var(--ink);
  }
  .ad{position:absolute;background:var(--white);overflow:hidden;box-shadow:0 6px 14px rgba(0,0,0,.28)}
  .ad--red{--accent:var(--red);--accent-light:var(--red-light);--pointer:var(--ink)}
  .ad--dark{--accent:var(--dark);--accent-light:var(--dark-light);--pointer:var(--red)}
  .ad--wide{width:535px;height:298px}
  .ad--square{width:536px;height:536px}

  .pitch{position:absolute;color:var(--white);border-radius:0 0 12px 12px;
    background:radial-gradient(ellipse at 55% 0%,var(--accent-light) 0%,var(--accent) 60%)}
  .pitch__question{font-family:"Rubik",sans-serif;font-weight:500}
  .pitch__call{font-family:"Nunito",sans-serif;font-weight:900}

  .benefits__title{position:absolute;font-family:"Rubik",sans-serif;font-weight:600;color:var(--accent)}
  .ad--dark .benefits__title{color:var(--ink)}
  .benefits{position:absolute;list-style:none;font-weight:300;color:#222}
  .benefits li{position:relative;white-space:nowrap}
  .benefits svg{position:absolute;left:0;color:var(--accent)}

  .photo-frame{position:absolute;border:2px solid var(--accent);background:var(--white)}
  .photo{position:absolute;background:linear-gradient(160deg,var(--photo-a) 0%,#9d9c98 35%,var(--photo-b) 65%,var(--photo-c) 100%)}

  .web{position:absolute;border-radius:999px;background:var(--accent);color:var(--white);
    font-family:"Rubik",sans-serif;font-weight:500;text-align:center;
    box-shadow:0 5px 0 rgba(0,0,0,.12)}
  .web__pointer{position:absolute;color:var(--pointer)}

  .brand{position:absolute;font-family:"Rubik",sans-serif;font-weight:600;color:var(--ink);white-space:nowrap}
  .corner{position:absolute;right:0;bottom:0;color:var(--accent)}

  /* wide format */
  .ad--wide .pitch{left:24px;top:0;width:266px;height:122px;padding:23px 0 0 18px}
  .ad--wide .pitch__question{font-size:13.2px;line-height:14.6px}
  .ad--wide .pitch__call{font-size:15.5px;margin-top:9px;letter-spacing:.1px}
  .ad--wide .brand{left:311px;top:38px;font-size:22px}
  .ad--wide .photo-frame{left:249px;top:74px;width:254px;height:154px;border-radius:14px}
  .ad--wide .photo{left:4px;top:4px;right:4px;bottom:4px;border-radius:10px}
  .ad--wide .benefits__title{left:36px;top:136px;font-size:13.2px}
  .ad--wide .benefits{left:40px;top:155px;font-size:11.4px;line-height:16.6px}
  .ad--wide .benefits li{padding-left:12px}
  .ad--wide .benefits svg{top:4px;width:8px;height:8px}
  .ad--wide .web{left:300px;top:240px;width:174px;height:32px;line-height:32px;font-size:14.5px}
  .ad--wide .web__pointer{left:456px;top:264px;width:16px;height:18px}

  /* square format */
  .ad--square .pitch{left:25px;top:0;width:257px;height:194px;padding:30px 0 0 24px}
  .ad--square .pitch__question{font-size:16.2px;line-height:16.6px}
  .ad--square .pitch__call{font-size:30px;line-height:30px;margin-top:8px}
  .ad--square .benefits__title{left:301px;top:32px;font-size:15.6px}
  .ad--square .benefits{left:305px;top:54px;font-size:12.7px;line-height:17.1px}
  .ad--square .benefits li{padding-left:12px}
  .ad--square .benefits svg{top:5px;width:8px;height:8px}
  .ad--square .photo-frame{left:25px;top:210px;width:486px;height:225px;border-radius:20px}
  .ad--square .photo{left:6px;top:6px;right:6px;bottom:6px;border-radius:14px}
  .ad--square .web{left:25px;top:452px;width:256px;height:46px;line-height:46px;font-size:22.5px}
  .ad--square .web__pointer{left:258px;top:488px;width:22px;height:24px}
  .ad--square .brand{left:316px;top:474px;font-size:20px}
</style>
</head>
<body>
<svg width="0" height="0" style="position:absolute" aria-hidden="true">
  <symbol id="tick" viewBox="0 0 10 10"><circle cx="5" cy="5" r="5" fill="currentColor"/><path d="M2.8 5.1 4.4 6.6 7.3 3.6" fill="none" stroke="#fff" stroke-width="1.4" stroke-linecap="round" stroke-linejoin="round"/></symbol>
  <symbol id="pointer" viewBox="0 0 20 22"><path d="M4 3 L4 17 L7.6 13.6 L10.4 20 L13 18.9 L10.3 12.6 L15.2 12.3 Z" fill="#fff" stroke="currentColor" stroke-width="1.6" stroke-linejoin="round"/></symbol>
</svg>

<!-- 90 x 50 mm, colour -->
<article class="ad ad--wide ad--red" style="left:55px;top:132px">
  <svg class="corner" width="535" height="298" viewBox="0 0 535 298" aria-hidden="true"><path d="M535 230 Q525 292 432 298 L535 298 Z" fill="currentColor"/></svg>
  <div class="pitch">
    <p class="pitch__question">Du arbeitest selbständig und<br>verantwortungsbewusst,<br>hast Freude am Kundenkontakt und<br>kannst jedes Problem lösen?</p>
    <p class="pitch__call">Dann komm direkt zu uns !</p>
  </div>
  <p class="brand">Fliesen-Worlak</p>
  <div class="photo-frame"><div class="photo" role="img" aria-label="Foto einer modernen Küche mit Esstisch, schwarzen Stühlen und grauen Bodenfliesen"></div></div>
  <h2 class="benefits__title">Das erwartet Dich bei uns:</h2>
  <ul class="benefits">
    <li><svg><use href="#tick"/></svg>Junges eingespieltes Team</li>
    <li><svg><use href="#tick"/></svg>Sehr gutes Betriebsklima</li>
    <li><svg><use href="#tick"/></svg>Faire Bezahlung</li>
    <li><svg><use href="#tick"/></svg>Baustellenfahrzeug + Werkzeug</li>
    <li><svg><use href="#tick"/></svg>Unbefristetes Arbeitsverhältnis</li>
    <li><svg><use href="#tick"/></svg>Heimatnahe Baustellen</li>
    <li><svg><use href="#tick"/></svg>Öffentliche, Gewerbliche, Private Baustellen</li>
  </ul>
  <p class="web">www.fliesen-worlak.de</p>
  <svg class="web__pointer" aria-hidden="true"><use href="#pointer"/></svg>
</article>

<!-- 90 x 50 mm, black & white -->
<article class="ad ad--wide ad--dark" style="left:611px;top:132px">
  <svg class="corner" width="535" height="298" viewBox="0 0 535 298" aria-hidden="true"><path d="M535 230 Q525 292 432 298 L535 298 Z" fill="currentColor"/></svg>
  <div class="pitch">
    <p class="pitch__question">Du arbeitest selbständig und<br>verantwortungsbewusst,<br>hast Freude am Kundenkontakt und<br>kannst jedes Problem lösen?</p>
    <p class="pitch__call">Dann komm direkt zu uns !</p>
  </div>
  <p class="brand">Fliesen-Worlak</p>
  <div class="photo-frame"><div class="photo" role="img" aria-label="Foto einer modernen Küche mit Esstisch, schwarzen Stühlen und grauen Bodenfliesen"></div></div>
  <h2 class="benefits__title">Das erwartet Dich bei uns:</h2>
  <ul class="benefits">
    <li><svg><use href="#tick"/></svg>Junges eingespieltes Team</li>
    <li><svg><use href="#tick"/></svg>Sehr gutes Betriebsklima</li>
    <li><svg><use href="#tick"/></svg>Faire Bezahlung</li>
    <li><svg><use href="#tick"/></svg>Baustellenfahrzeug + Werkzeug</li>
    <li><svg><use href="#tick"/></svg>Unbefristetes Arbeitsverhältnis</li>
    <li><svg><use href="#tick"/></svg>Heimatnahe Baustellen</li>
    <li><svg><use href="#tick"/></svg>Öffentliche, Gewerbliche, Private Baustellen</li>
  </ul>
  <p class="web">www.fliesen-worlak.de</p>
  <svg class="web__pointer" aria-hidden="true"><use href="#pointer"/></svg>
</article>

<!-- 90 x 90 mm, colour -->
<article class="ad ad--square ad--red" style="left:54px;top:449px">
  <svg class="corner" width="536" height="536" viewBox="0 0 536 536" aria-hidden="true"><path d="M536 448 Q526 528 470 536 L536 536 Z" fill="currentColor"/></svg>
  <div class="pitch">
    <p class="pitch__question">Du arbeitest selbständig<br>und verantwortungsbewusst,<br>hast Freude am<br>Kundenkontakt und kannst<br>jedes Problem lösen?</p>
    <p class="pitch__call">Dann komm<br>direkt zu uns !</p>
  </div>
  <h2 class="benefits__title">Das erwartet Dich bei uns:</h2>
  <ul class="benefits">
    <li><svg><use href="#tick"/></svg>Junges eingespieltes Team</li>
    <li><svg><use href="#tick"/></svg>Sehr gutes Betriebsklima</li>
    <li><svg><use href="#tick"/></svg>Faire Bezahlung</li>
    <li><svg><use href="#tick"/></svg>Baustellenfahrzeug + Werkzeug</li>
    <li><svg><use href="#tick"/></svg>Unbefristetes Arbeitsverhältnis</li>
    <li><svg><use href="#tick"/></svg>Heimatnahe Baustellen</li>
    <li><svg><use href="#tick"/></svg>Öffentliche, Gewerbliche, Private<br>Baustellen</li>
  </ul>
  <div class="photo-frame"><div class="photo" role="img" aria-label="Foto einer modernen Küche mit Esstisch, schwarzen Stühlen und grauen Bodenfliesen"></div></div>
  <p class="web">www.fliesen-worlak.de</p>
  <svg class="web__pointer" aria-hidden="true"><use href="#pointer"/></svg>
  <p class="brand">Fliesen-Worlak</p>
</article>

<!-- 90 x 90 mm, black & white -->
<article class="ad ad--square ad--dark" style="left:611px;top:449px">
  <svg class="corner" width="536" height="536" viewBox="0 0 536 536" aria-hidden="true"><path d="M536 448 Q526 528 470 536 L536 536 Z" fill="currentColor"/></svg>
  <div class="pitch">
    <p class="pitch__question">Du arbeitest selbständig<br>und verantwortungsbewusst,<br>hast Freude am<br>Kundenkontakt und kannst<br>jedes Problem lösen?</p>
    <p class="pitch__call">Dann komm<br>direkt zu uns !</p>
  </div>
  <h2 class="benefits__title">Das erwartet Dich bei uns:</h2>
  <ul class="benefits">
    <li><svg><use href="#tick"/></svg>Junges eingespieltes Team</li>
    <li><svg><use href="#tick"/></svg>Sehr gutes Betriebsklima</li>
    <li><svg><use href="#tick"/></svg>Faire Bezahlung</li>
    <li><svg><use href="#tick"/></svg>Baustellenfahrzeug + Werkzeug</li>
    <li><svg><use href="#tick"/></svg>Unbefristetes Arbeitsverhältnis</li>
    <li><svg><use href="#tick"/></svg>Heimatnahe Baustellen</li>
    <li><svg><use href="#tick"/></svg>Öffentliche, Gewerbliche, Private<br>Baustellen</li>
  </ul>
  <div class="photo-frame"><div class="photo" role="img" aria-label="Foto einer modernen Küche mit Esstisch, schwarzen Stühlen und grauen Bodenfliesen"></div></div>
  <p class="web">www.fliesen-worlak.de</p>
  <svg class="web__pointer" aria-hidden="true"><use href="#pointer"/></svg>
  <p class="brand">Fliesen-Worlak</p>
</article>
</body>
</html>
```